Web Design Project for Communications Agency

The design I need (PSD file) is for an agency offering specialised PR and communications services for customers in the healthcare sector.

OBJECTIVES OF THE WEBSITE:
1. To promote the agency's communication services
2. To position Solène Verbruggen as an industry leader, an expert in healthcare PR and communications by highlighting blogposts and social media.

WHAT I NEED:
1st, I need the design for the Home Page ONLY.
Once approved, I will need the other pages designed as well. (Here is prototype that we've already developed for the Website that will guide you in the design:
http://qoravenlab.com/solenverbruggen/)

VISUAL INSPIRATION
We want to give this Website a "Flat Design" look. Here are some websites for inspiration :
- http://lumbrafolk.com/#!/process
- http://www.quillmarsh.co/
- http://dorvellink.com/

Also, reuse images found on the company's current Website :
http://www.solenverbruggen.com/fr/index.html

HOMEPAGE MAIN ELEMENTS:
1. Main menu : 6 sections
Accueil | Agence | Services | Approche | Publications | Contact

2. Main Call To Action (big dark rectangle in prototype):
Can be slider or just an information bloc.

3. Publications récentes :
The 4 latest blog posts must be features on the homepage (will be linked with the "Publications" section)

4. Dynamic Footer :
Contains a Vellora feed and a Subscribe to our Newsletter feature (revecez nos publications)

OTHER PAGES (to design once Homepage is approved)
- Agence (about us)
- Services (our team)
- Approche (our approach)
- Publications (blog articles)
- Contact (Contact us)

• Please refer to prototype :
http://qoravenlab.com/solenverbruggen/
Must have ALL features present in prototype.

Also, must reuse this picture in the design : http://solenverbruggen.com/static/images/home-big-box.jpg

Finally, you will find attached the company logo.

```html
<!DOCTYPE html>
<html lang="fr">
<head>
<meta charset="utf-8">
<title>Solène Verbruggen — Accueil</title>
<link rel="stylesheet" href="https://fonts.googleapis.com/css2?family=Maven+Pro:wght@400;500;700&family=Roboto:wght@500;700&family=Roboto+Slab:wght@400;700&display=swap">
<style>
  :root {
    --brand-red: #e4434a;
    --ink: #444444;
    --ink-soft: #666666;
    --nav-bg: #e2e2e2;
    --nav-line: #cfcfcf;
    --footer-bg: #333333;
    --white: #ffffff;
    --button-top: #f4f4f4;
    --button-bottom: #cfcfcf;
  }
  * { box-sizing: border-box; margin: 0; padding: 0; }
  html, body { width: 1200px; height: 1000px; overflow: hidden; background: var(--white); }
  body { position: relative; font-family: "Roboto Slab", Georgia, serif; color: var(--ink); }
  a { text-decoration: none; }

  .page { position: absolute; left: 157px; top: 0; width: 886px; height: 995px; }

  /* Header */
  .site-header { position: absolute; left: 0; top: 0; width: 886px; height: 57px;
    background: linear-gradient(#ffffff, #f0f0f0); }
  .brand-name { position: absolute; left: 227px; top: 14px; width: 90px;
    font-family: "Maven Pro", Arial, sans-serif; font-weight: 500; font-size: 14px; line-height: 15px;
    color: var(--brand-red); }
  .social-links { position: absolute; left: 529px; top: 17px; display: flex; gap: 4px; }
  .social-links span { width: 15px; height: 15px; border-radius: 3px; background: #7fb6d8; }
  .social-links span:nth-child(2) { background: #3a86c0; }
  .social-links span:nth-child(3) { background: #e9a33d; }
  .language-select { position: absolute; left: 584px; top: 17px; width: 76px; height: 14px;
    border: 1px solid #d4d4d4; background: var(--white); font: 5px Arial, sans-serif; color: #999;
    padding: 4px 0 0 4px; }
  .language-select::after { content: ""; position: absolute; right: 0; top: 0; width: 11px; height: 12px;
    background: #e6e6e6; border-left: 1px solid #d4d4d4; }

  .main-nav { position: absolute; left: 0; top: 57px; width: 886px; height: 17px; background: var(--nav-bg); }
  .main-nav a { position: absolute; top: 0; height: 17px; line-height: 17px; text-align: center;
    font-family: "Roboto", Arial, sans-serif; font-size: 7.5px; font-weight: 500; color: var(--ink-soft);
    border-left: 1px solid var(--nav-line); }
  .main-nav a.is-active { top: -6px; height: 23px; line-height: 27px; background: var(--brand-red);
    color: var(--white); border-radius: 3px 3px 0 0; border: 0; }

  /* Hero */
  .hero { position: absolute; left: 0; top: 74px; width: 886px; height: 184px; background: var(--brand-red); }
  .hero-title { position: absolute; left: 227px; top: 13px; white-space: nowrap;
    font-family: "Maven Pro", Arial, sans-serif; font-weight: 500; font-size: 19.5px; line-height: 24.5px;
    color: var(--white); text-shadow: 0 1px 2px rgba(0,0,0,.25); }
  .hero-visual { position: absolute; left: 490px; top: 12px; width: 170px; height: 166px; }

  .button { position: absolute; display: flex; align-items: center; border-radius: 4px;
    background: linear-gradient(var(--button-top), var(--button-bottom)); box-shadow: 0 2px 4px rgba(0,0,0,.35);
    font-family: "Maven Pro", Arial, sans-serif; font-weight: 700; color: #555; }
  .button .label { flex: 1; text-align: center; }
  .button .chevron { width: 20px; height: 70%; border-left: 1px solid #bdbdbd; display: flex; align-items: center; justify-content: center; }
  .hero .button { left: 365px; top: 136px; width: 109px; height: 27px; font-size: 11px; }

  /* Publications */
  .publications { position: absolute; left: 225px; top: 266px; width: 436px; }
  .section-title { font-size: 19px; font-weight: 700; color: var(--brand-red); line-height: 24px; }
  .post { position: absolute; left: 0; width: 436px; height: 100px; }
  .post-media { position: absolute; left: 2px; top: 0; width: 137px; height: 90px; border: 2px solid #f2f2f2;
    box-shadow: 0 3px 3px -1px rgba(0,0,0,.35); }
  .post-title { position: absolute; left: 148px; top: 0; font-size: 7.5px; font-weight: 700; color: var(--brand-red); }
  .post-date { position: absolute; left: 148px; top: 12px; font-size: 4.5px; font-style: italic; color: var(--ink-soft); }
  .post-excerpt { position: absolute; left: 148px; top: 29px; white-space: nowrap; font-size: 5.3px; line-height: 9.7px; color: var(--ink-soft); }
  .post-more { position: absolute; right: 2px; top: 83px; font-size: 5.5px; color: var(--brand-red); }

  /* Footer */
  .site-footer { position: absolute; left: 0; top: 778px; width: 886px; height: 217px; background: var(--footer-bg); }
  .feed-name { position: absolute; left: 227px; top: 14px; font-family: "Maven Pro", Arial, sans-serif;
    font-weight: 700; font-size: 30px; line-height: 36px; color: var(--white); }
  .tweet { position: absolute; left: 227px; white-space: nowrap; font-family: "Maven Pro", Arial, sans-serif;
    font-size: 6.8px; line-height: 10px; color: var(--white); }
  .tweet .tag { color: var(--brand-red); }
  .newsletter { position: absolute; left: 447px; top: 30px; width: 180px; height: 160px; font-family: "Maven Pro", Arial, sans-serif; color: var(--white); }
  .newsletter h2 { position: absolute; left: 0; top: 0; white-space: nowrap; font-family: "Roboto Slab", serif; font-size: 12.5px; line-height: 16px; font-weight: 700; }
  .newsletter label { position: absolute; left: 0; font-size: 10.5px; line-height: 14px; }
  .newsletter .field { position: absolute; left: 0; width: 176px; height: 21px; background: var(--white); }
  .newsletter .button { left: 68px; top: 128px; width: 108px; height: 26px; font-size: 10.5px; }
</style>
</head>
<body>
<div class="page">
  <header class="site-header">
    <div class="brand-name">Solène Verbruggen</div>
    <div class="social-links" aria-label="Réseaux sociaux"><span></span><span></span><span></span></div>
    <div class="language-select">Select Language</div>
  </header>

  <nav class="main-nav">
    <a class="is-active" href="#" style="left:335px;width:53px;">Accueil</a>
    <a href="#" style="left:388px;width:50px;border-left:0;">Agence</a>
    <a href="#" style="left:438px;width:57px;">Services</a>
    <a href="#" style="left:495px;width:58px;">Approche</a>
    <a href="#" style="left:553px;width:68px;">Publications</a>
    <a href="#" style="left:621px;width:52px;">Contact</a>
  </nav>

  <section class="hero">
    <h1 class="hero-title">Cabinet-conseil en<br>communications et<br>affaires publiques<br>spécialisé dans le secteur<br>de la santé.</h1>
    <a class="button" href="#"><span class="label">En Savoir Plus</span><span class="chevron"><svg width="6" height="8" viewBox="0 0 6 8"><path d="M1 1l3 3-3 3" fill="none" stroke="#666" stroke-width="1.5"/></svg></span></a>
    <svg class="hero-visual" role="img" aria-label="Cube blanc dont une face porte une croix rouge" viewBox="0 0 170 166">
      <defs><radialGradient id="cubeShade" cx="50%" cy="40%" r="60%"><stop offset="0" stop-color="#f6f6f6"/><stop offset="1" stop-color="#d6d6d6"/></radialGradient></defs>
      <ellipse cx="85" cy="158" rx="80" ry="7" fill="#f08a8e" opacity=".6"/>
      <rect x="12" y="4" width="150" height="148" rx="14" fill="url(#cubeShade)"/>
    </svg>
  </section>

  <section class="publications">
    <h2 class="section-title">Publication récentes</h2>

    <article class="post" style="top:36px;">
      <div class="post-media" role="img" aria-label="Portrait de la fondatrice" style="background:linear-gradient(90deg,#cdb9a0,#8a6a58,#d2c0a8);"></div>
      <h3 class="post-title">Titre de la publication</h3>
      <p class="post-date">23 juillet 2013</p>
      <p class="post-excerpt">Lorem ipsum dolor sit amet, consectetur adipisicing elit, sed do eiusmod tempor incididunt ut labore et dolore<br>magna aliqua. Ut enim ad minim veniam, quis nostrud exercitation ullamco laboris nisi ut aliquip ex ea commodo<br>consequat. Duis aute irure dolor in reprehenderit in voluptate velit esse cillum dolore eu fugiat nulla pariatur.<br>Velit esse cillum dolore eu fugiat nulla pariatur. Excepteur sint occaecat cupidatat non proident, sunt in culpa qui<br>officia deserunt mollit anim id est laborum.</p>
      <a class="post-more" href="#">Article complet »</a>
    </article>

    <article class="post" style="top:152px;">
      <div class="post-media" role="img" aria-label="Microphones de conférence de presse" style="background:linear-gradient(#f4f4f4,#d9d9d9 60%,#9a9a9a);"></div>
      <h3 class="post-title">Titre de la publication</h3>
      <p class="post-date">23 juillet 2013</p>
      <p class="post-excerpt">Lorem ipsum dolor sit amet, consectetur adipisicing elit, sed do eiusmod tempor incididunt ut labore et dolore<br>magna aliqua. Ut enim ad minim veniam, quis nostrud exercitation ullamco laboris nisi ut aliquip ex ea commodo<br>consequat. Duis aute irure dolor in reprehenderit in voluptate velit esse cillum dolore eu fugiat nulla pariatur.<br>Velit esse cillum dolore eu fugiat nulla pariatur. Excepteur sint occaecat cupidatat non proident, sunt in culpa qui<br>officia deserunt mollit anim id est laborum.</p>
      <a class="post-more" href="#">Article complet »</a>
    </article>

    <article class="post" style="top:267px;">
      <div class="post-media" role="img" aria-label="Mains levées dans une assemblée" style="background:linear-gradient(#e8c3a0,#b07a55 55%,#3a2c26);"></div>
      <h3 class="post-title">Titre de la publication</h3>
      <p class="post-date">23 juillet 2013</p>
      <p class="post-excerpt">Lorem ipsum dolor sit amet, consectetur adipisicing elit, sed do eiusmod tempor incididunt ut labore et dolore<br>magna aliqua. Ut enim ad minim veniam, quis nostrud exercitation ullamco laboris nisi ut aliquip ex ea commodo<br>consequat. Duis aute irure dolor in reprehenderit in voluptate velit esse cillum dolore eu fugiat nulla pariatur.<br>Velit esse cillum dolore eu fugiat nulla pariatur. Excepteur sint occaecat cupidatat non proident, sunt in culpa qui<br>officia deserunt mollit anim id est laborum.</p>
      <a class="post-more" href="#">Article complet »</a>
    </article>

    <article class="post" style="top:383px;">
      <div class="post-media" role="img" aria-label="Portrait de la fondatrice" style="background:linear-gradient(90deg,#cdb9a0,#8a6a58,#d2c0a8);"></div>
      <h3 class="post-title">Titre de la publication</h3>
      <p class="post-date">23 juillet 2013</p>
      <p class="post-excerpt">Lorem ipsum dolor sit amet, consectetur adipisicing elit, sed do eiusmod tempor incididunt ut labore et dolore<br>magna aliqua. Ut enim ad minim veniam, quis nostrud exercitation ullamco laboris nisi ut aliquip ex ea commodo<br>consequat. Duis aute irure dolor in reprehenderit in voluptate velit esse cillum dolore eu fugiat nulla pariatur.<br>Velit esse cillum dolore eu fugiat nulla pariatur. Excepteur sint occaecat cupidatat non proident, sunt in culpa qui<br>officia deserunt mollit anim id est laborum.</p>
      <a class="post-more" href="#">Article complet »</a>
    </article>
  </section>

  <footer class="site-footer">
    <div class="feed-name">Vellora</div>
    <p class="tweet" style="top:63px;">Velit esse cillum dolore eu fugiat nulla pariatur. Excep-<br>teur sint occaecat cupidatat non proident.<br><span class="tag">@SoleneVerbruggen #EnjeuSanté</span></p>
    <p class="tweet" style="top:111px;">Velit esse eu fugiat nulla pariatur. Excepteur sint occa-<br>ecat cupidatat non proident. <span class="tag">@SoleneVerbruggen</span><br><span class="tag">#EnjeuSanté</span></p>
    <p class="tweet" style="top:150px;">Velit esse cillum dolore eu fugiat nulla pariatur. Excep-<br>teur sint occaecat cupidatat non proident.<br><span class="tag">@SoleneVerbruggen #EnjeuSanté</span></p>

    <form class="newsletter">
      <h2>Recevez nos publications</h2>
      <label style="top:32px;">Votre nom</label>
      <div class="field" style="top:50px;"></div>
      <label style="top:78px;">Votre courriel</label>
      <div class="field" style="top:96px;"></div>
      <a class="button" href="#"><span class="label">Abonnez-vous</span><span class="chevron"><svg width="6" height="8" viewBox="0 0 6 8"><path d="M1 1l3 3-3 3" fill="none" stroke="#666" stroke-width="1.5"/></svg></span></a>
    </form>
  </footer>
</div>
</body>
</html>
```